Lantern Hearthworks Business Cards

Looking to create simple business cards that highlight our unique three sided triangle fire pit design with the colors and font of our logo, listed below.

Requirements
Must have
• Looking for something simple that includes a picture of our fire pit with name, website (lanternhearthworks.com), phone number and email. Want to keep the color mostly orange and black.
• Font is gotham(medium) and orange color code is #ee6e22

```html
<!DOCTYPE html>
<html lang="en">
<head>
<meta charset="utf-8">
<title>Lantern Hearthworks Business Cards</title>
<link rel="stylesheet" href="https://fonts.googleapis.com/css2?family=Montserrat:wght@400;500;600&display=swap">
<style>
  :root {
    --orange: #ee6e22;
    --ink: #1b1b1b;
    --grey: #7a7a7a;
    --text-grey: #6a6a6a;
    --paper: #ffffff;
    --backdrop: #e9e9e7;
  }
  * { margin: 0; padding: 0; box-sizing: border-box; }
  html, body { width: 1200px; height: 913px; overflow: hidden; }
  body {
    background: var(--backdrop);
    font-family: "Montserrat", Arial, sans-serif;
    position: relative;
  }
  .card {
    position: absolute;
    width: 620px;
    height: 354px;
    border-radius: 3px;
    box-shadow: 0 10px 24px rgba(0,0,0,.18);
    overflow: hidden;
  }
  .card--front { left: 70px; top: 60px; background: var(--ink); }
  .card--back { left: 510px; top: 500px; background: var(--paper); }

  /* front */
  .front-brand {
    position: absolute; left: 130px; top: 112px;
    display: flex; align-items: center; gap: 26px;
  }
  .brand-square { width: 44px; height: 44px; background: var(--orange); flex: none; }
  .divider { width: 1px; background: var(--grey); }
  .front-brand .divider { height: 130px; }
  .brand-name {
    color: var(--orange); font-weight: 500;
    text-transform: uppercase; letter-spacing: .22em;
    line-height: 1.15;
  }
  .front-brand .brand-name { font-size: 34px; }

  /* back */
  .back-brand {
    position: absolute; left: 56px; top: 150px;
    display: flex; align-items: center; gap: 14px;
    width: 226px;
  }
  .back-brand .brand-square { width: 26px; height: 26px; }
  .back-brand .brand-name { font-size: 17px; letter-spacing: .14em; }
  .back-card__divider {
    position: absolute; left: 300px; top: 98px; height: 168px;
  }
  .contact { position: absolute; left: 322px; top: 92px; color: var(--text-grey); }
  .contact__name {
    color: var(--orange); font-weight: 600; font-size: 21px;
    text-transform: uppercase; letter-spacing: .01em;
  }
  .contact__role { font-size: 13px; margin-top: 2px; }
  .contact__address { font-size: 13px; margin-top: 12px; line-height: 1.35; }
  .contact__lines { list-style: none; margin-top: 10px; font-size: 13px; line-height: 1.5; }
  .contact__lines li { display: flex; align-items: center; gap: 9px; }
  .contact__lines svg { width: 12px; height: 12px; fill: var(--orange); flex: none; }
</style>
</head>
<body>

<section class="card card--front" aria-label="Card front">
  <div class="front-brand">
    <span class="brand-square" aria-hidden="true"></span>
    <span class="divider" aria-hidden="true"></span>
    <p class="brand-name">Lantern<br>Hearthworks</p>
  </div>
</section>

<section class="card card--back" aria-label="Card back">
  <div class="back-brand">
    <span class="brand-square" aria-hidden="true"></span>
    <p class="brand-name">Lantern<br>Hearthworks</p>
  </div>
  <span class="divider back-card__divider" aria-hidden="true"></span>
  <div class="contact">
    <p class="contact__name">Elena Varga</p>
    <p class="contact__role">Director</p>
    <p class="contact__address">48 Ember Lane<br>272 Riverton, Spain</p>
    <ul class="contact__lines">
      <li>
        <svg viewBox="0 0 24 24" aria-hidden="true"><path d="M6.6 10.8a15.1 15.1 0 0 0 6.6 6.6l2.2-2.2a1 1 0 0 1 1-.25 11.4 11.4 0 0 0 3.6.57 1 1 0 0 1 1 1V20a1 1 0 0 1-1 1A17 17 0 0 1 3 4a1 1 0 0 1 1-1h3.5a1 1 0 0 1 1 1c0 1.250.2 2.45.57 3.6a1 1 0 0 1-.25 1z"/></svg>
        5550142788
      </li>
      <li>
        <svg viewBox="0 0 24 24" aria-hidden="true"><path d="M7 1h10a2 2 0 0 1 2 2v18a2 2 0 0 1-2 2H7a2 2 0 0 1-2-2V3a2 2 0 0 1 2-2zm0 3v14h10V4zm5 15.5a1.2 1.2 0 1 0 0 2.4 1.2 1.2 0 0 0 0-2.4z"/></svg>
        5550193604
      </li>
      <li>
        <svg viewBox="0 0 24 24" aria-hidden="true"><path d="M2 5h20v14H2zm2 2v.4l8 5.2 8-5.2V7zm0 2.8V17h16V9.8l-8 5.2z"/></svg>
        info@lanternhearthworks.com
      </li>
      <li>
        <svg viewBox="0 0 24 24" aria-hidden="true"><path d="M12 2a10 10 0 1 0 0 20 10 10 0 0 0 0-20zm6.9 6h-3a15.7 15.7 0 0 0-1.3-3.6A8 8 0 0 1 18.9 8zM12 4c.8 1.2 1.5 2.5 1.9 4h-3.8c.4-1.5 1.1-2.8 1.9-4zM4.3 14a8 8 0 0 1 0-4h3.4a16 16 0 0 0 0 4zm.8 2h3a15.7 15.7 0 0 0 1.3 3.6A8 8 0 0 1 5.1 16zm3-8h-3a8 8 0 0 1 4.3-3.6A15.7 15.7 0 0 0 8.1 8zM12 20c-.8-1.2-1.5-2.5-1.9-4h3.8c-.4 1.5-1.1 2.8-1.9 4zm2.3-6H9.7a14.6 14.6 0 0 1 0-4h4.6a14.6 14.6 0 0 1 0 4zm.3 5.6a15.7 15.7 0 0 0 1.3-3.6h3a8 8 0 0 1-4.3 3.6zM16.3 14a16 16 0 0 0 0-4h3.4a8 8 0 0 1 0 4z"/></svg>
        www.lanternhearthworks.com
      </li>
    </ul>
  </div>
</section>

</body>
</html>
```